wine trade consumer promotion in retail stores in the Bahamas

We need to create a poster that calls clients to action. We are a wine company in the Bahamas that needs to come across as the place to buy wines. It needs to be very authoritative and clear. that this is about making time for wine and you can try before you buy. So make Time For Wine is the lead message with graphics and the - wine of the month...try before you buy is the 2nd element.
Updates
I need ideas by Sunday 3rd October please .
Thank you
Target Market(s)
Local affluent clientele
Industry/Entity Type
wine
Other font styles liked:
- let the designer choose- look at wine companies website
Requirements
Must have
- The heading must be ¨Make Time For Wine¨ , secondary message ¨Wine Of The Month- Try Before you Buy¨- Try before you buy¨ Lots of wine images not bottles but grapes red /white,
Nice to have
- Images from vineyards around the parameters, clear messages that make you think about wine. Look at wine production sites to get an idea.
Should not have
- no palm trees or anything to do with the Caribbean, no people , no sunshine, no beaches.

```html
<!DOCTYPE html>
<html lang="en">
<head>
<meta charset="utf-8">
<title>Make Time For Wine – Wine of the Month</title>
<link href="https://fonts.googleapis.com/css2?family=Yellowtail&family=Josefin+Sans:wght@400&family=Lato:ital,wght@1,400&display=swap" rel="stylesheet">
<style>
  :root {
    --vine-deep: #1f2a18;
    --vine-mid: #3d4e2c;
    --vine-light: #6f7f4c;
    --grape-glow: #b9b77a;
    --shadow-band: #1a2114;
    --ink: #ffffff;
    --sketch: rgba(255, 255, 255, 0.22);
  }
  * { margin: 0; padding: 0; box-sizing: border-box; }
  html, body {
    width: 849px; height: 1200px; overflow: hidden;
    background: var(--vine-deep);
  }
  .poster {
    position: relative;
    width: 849px; height: 1200px;
    overflow: hidden;
  }
  .vineyard-photo {
    position: absolute; inset: 0;
    background:
      radial-gradient(ellipse 220px 300px at 430px 600px, var(--grape-glow) 0%, rgba(185,183,122,0.35) 45%, transparent 75%),
      radial-gradient(ellipse 380px 460px at 420px 520px, var(--vine-light) 0%, var(--vine-mid) 60%, transparent 100%),
      linear-gradient(160deg, var(--vine-mid) 0%, var(--vine-deep) 100%);
  }
  .shadow-band {
    position: absolute; left: 0; right: 0; bottom: 0; height: 300px;
    background: linear-gradient(to bottom, rgba(26,33,20,0) 0%, rgba(26,33,20,0.85) 45%, var(--shadow-band) 100%);
  }
  .sketch {
    position: absolute;
    background: var(--sketch);
    border-radius: 50%;
  }
  .sketch--bunch { left: 100px; top: 460px; width: 150px; height: 175px; border-radius: 45% 45% 50% 50%; }
  .sketch--leaf-top { left: 510px; top: 125px; width: 150px; height: 240px; border-radius: 40%; }
  .sketch--leaf-left { left: 200px; top: 600px; width: 95px; height: 85px; }
  .sketch--leaf-right { left: 610px; top: 525px; width: 120px; height: 110px; }
  .sketch--berries-right { left: 672px; top: 412px; width: 55px; height: 60px; }
  .sketch--berries-mid { left: 445px; top: 322px; width: 50px; height: 50px; }
  .sketch--berries-low-left { left: 165px; top: 800px; width: 60px; height: 55px; }
  .sketch--berries-low { left: 440px; top: 835px; width: 70px; height: 70px; }
  .sketch--flourish { left: 205px; top: 200px; width: 85px; height: 80px; }

  .headline {
    position: absolute; left: 0; top: 0; width: 849px; height: 900px;
    font-family: "Yellowtail", cursive;
    color: var(--ink);
    font-weight: 400;
  }
  .headline span {
    position: absolute; display: block; line-height: 1; white-space: nowrap;
    transform: rotate(-9deg);
  }
  .headline__make { left: 185px; top: 268px; font-size: 132px; }
  .headline__time { left: 285px; top: 360px; font-size: 250px; }
  .headline__for  { left: 400px; top: 565px; font-size: 90px; }
  .headline__wine { left: 235px; top: 640px; font-size: 240px; }

  .offer {
    position: absolute; left: 0; right: 0; top: 1022px;
    text-align: center; color: var(--ink);
  }
  .offer__title {
    font-family: "Josefin Sans", sans-serif;
    font-size: 50px; font-weight: 400; letter-spacing: 0.5px;
    line-height: 1;
  }
  .offer__tagline {
    margin-top: 14px;
    display: flex; justify-content: center; align-items: center; gap: 14px;
  }
  .offer__tagline p {
    font-family: "Lato", sans-serif;
    font-style: italic; font-size: 40px; line-height: 1;
  }
  .swash { width: 115px; height: 24px; }
  .swash--right { transform: scaleX(-1); }
</style>
</head>
<body>
<main class="poster">
  <div class="vineyard-photo" role="img" aria-label="Close-up photograph of white grape clusters hanging among green vine leaves in a vineyard"></div>
  <div class="shadow-band"></div>

  <div class="sketch sketch--bunch" role="img" aria-label="Line-drawn grape bunch ornament"></div>
  <div class="sketch sketch--leaf-top" role="img" aria-label="Line-drawn vine tendril and grape leaves ornament"></div>
  <div class="sketch sketch--leaf-left" role="img" aria-label="Line-drawn grape leaf ornament"></div>
  <div class="sketch sketch--leaf-right" role="img" aria-label="Line-drawn grape leaf ornament"></div>
  <div class="sketch sketch--berries-right" role="img" aria-label="Line-drawn grape berries ornament"></div>
  <div class="sketch sketch--berries-mid" role="img" aria-label="Line-drawn grape berries ornament"></div>
  <div class="sketch sketch--berries-low-left" role="img" aria-label="Line-drawn grape berries ornament"></div>
  <div class="sketch sketch--berries-low" role="img" aria-label="Line-drawn grape berries ornament"></div>
  <div class="sketch sketch--flourish" role="img" aria-label="Line-drawn crossed flourish ornament"></div>

  <h1 class="headline">
    <span class="headline__make">Make</span>
    <span class="headline__time">Time</span>
    <span class="headline__for">For</span>
    <span class="headline__wine">Wine</span>
  </h1>

  <section class="offer">
    <h2 class="offer__title">WINE OF THE MONTH</h2>
    <div class="offer__tagline">
      <svg class="swash swash--left" viewBox="0 0 115 24" aria-hidden="true">
        <path d="M2 14 C30 4, 60 22, 95 12 C104 9, 110 12, 106 17 C102 21, 96 17, 100 13" fill="none" stroke="#fff" stroke-width="3" stroke-linecap="round"/>
      </svg>
      <p>Try Before you Buy</p>
      <svg class="swash swash--right" viewBox="0 0 115 24" aria-hidden="true">
        <path d="M2 14 C30 4, 60 22, 95 12 C104 9, 110 12, 106 17 C102 21, 96 17, 100 13" fill="none" stroke="#fff" stroke-width="3" stroke-linecap="round"/>
      </svg>
    </div>
  </section>
</main>
</body>
</html>
```